Brackenfield Carpets Ltd

I'm looking for a modern looking business card with a logo that's relates to the business, maybe a sheep etc. I will need my name and phone numbers to be included

Industry/Entity Type

Business

Contact Information for Business Card

Tom Brackenfield, Director
Phone numbers mobile 07913 546208 and office 0161 735 2846
Carpets and flooring supplied and fitted

```html
<!DOCTYPE html>
<html lang="en">
<head>
<meta charset="utf-8">
<title>Brackenfield Carpets Ltd – Business Card</title>
<link href="https://fonts.googleapis.com/css2?family=Bebas+Neue&family=Montserrat:wght@300;400;600&display=swap" rel="stylesheet">
<style>
  :root {
    --backdrop: #d9d9d9;
    --paper: #efefef;
    --ink: #262422;
    --lime: #8ab51e;
    --white: #f4f4f4;
    --placeholder: #b9b9b9;
  }
  * { box-sizing: border-box; margin: 0; padding: 0; }
  html, body {
    width: 1200px; height: 900px; overflow: hidden;
    background: radial-gradient(circle at 40% 35%, #ececec, var(--backdrop));
    font-family: "Montserrat", sans-serif;
  }
  .card {
    position: absolute; top: 180px;
    width: 320px; height: 540px;
    overflow: hidden;
    box-shadow: 0 6px 18px rgba(0,0,0,.18);
  }
  .card--front { left: 240px; background: var(--paper); }
  .card--back  { left: 640px; background: var(--white); }

  .block { position: absolute; background: var(--ink); }
  .front__tab-top    { left: 0; top: 0; width: 140px; height: 50px; }
  .front__green-strip { position: absolute; left: 0; top: 66px; width: 150px; height: 410px; background: var(--lime); }
  .front__tab-bottom { right: 0; bottom: 0; width: 160px; height: 50px; }

  .nameplate {
    position: absolute; left: 70px; top: 105px; width: 250px; height: 100px;
    background: var(--ink); padding: 22px 0 0 22px;
  }
  .nameplate__name {
    font-family: "Bebas Neue", sans-serif; color: var(--white);
    font-size: 33px; line-height: 1; letter-spacing: .3px;
    white-space: nowrap;
  }
  .nameplate__role {
    font-family: "Bebas Neue", sans-serif; color: var(--lime);
    font-size: 19px; line-height: 1; letter-spacing: 1px; margin-top: 6px;
    white-space: nowrap;
  }

  .phone-icon { position: absolute; left: 136px; top: 296px; }
  .contact { position: absolute; left: 178px; top: 262px; color: var(--ink); }
  .contact__label { font-size: 13px; font-weight: 600; }
  .contact__number { font-size: 15px; font-weight: 400; margin-bottom: 18px; }

  .back__band-top { left: 0; top: 0; width: 100%; height: 62px; }
  .back__green { position: absolute; left: 0; top: 74px; width: 100%; height: 392px; background: var(--lime); }
  .back__band-bottom { left: 0; bottom: 0; width: 100%; height: 62px; }

  .logo-panel {
    position: absolute; left: 0; top: 200px; width: 285px; height: 150px;
    background: var(--ink);
  }
  .logo-panel__mascot {
    position: absolute; right: 30px; top: -50px; width: 120px; height: 105px;
    background: linear-gradient(160deg, #f2f2f2, var(--placeholder));
    border-radius: 40%;
  }
  .logo-panel__name {
    position: absolute; left: 16px; bottom: 42px;
    color: var(--white); font-size: 14.5px; font-weight: 400; letter-spacing: .2px;
    white-space: nowrap;
  }
  .logo-panel__tagline {
    position: absolute; left: 16px; bottom: 22px;
    color: var(--white); font-size: 11px; font-weight: 300;
    white-space: nowrap;
  }
</style>
</head>
<body>

<section class="card card--front" aria-label="Business card front">
  <div class="block front__tab-top"></div>
  <div class="front__green-strip"></div>
  <div class="nameplate">
    <div class="nameplate__name">Tom Brackenfield</div>
    <div class="nameplate__role">Director</div>
  </div>
  <svg class="phone-icon" width="28" height="28" viewBox="0 0 28 28" aria-hidden="true">
    <circle cx="14" cy="14" r="12" fill="none" stroke="#f4f4f4" stroke-width="1.6"/>
    <path d="M10 8.5c-1 .6-1.6 1.6-1 3.2 1 2.8 3.4 5.4 6.3 6.6 1.5.6 2.6 0 3.2-1l-2-2-1.4.8c-1.4-.7-2.6-2-3.2-3.4l.8-1.4z" fill="#f4f4f4"/>
  </svg>
  <div class="contact">
    <div class="contact__label">mobile:</div>
    <div class="contact__number">07913 546208</div>
    <div class="contact__label">office:</div>
    <div class="contact__number">0161 735 2846</div>
  </div>
  <div class="block front__tab-bottom"></div>
</section>

<section class="card card--back" aria-label="Business card back">
  <div class="block back__band-top"></div>
  <div class="back__green"></div>
  <div class="logo-panel">
    <div class="logo-panel__mascot" role="img" aria-label="Illustration of a woolly sheep mascot"></div>
    <div class="logo-panel__name">BRACKENFIELD CARPETS LTD</div>
    <div class="logo-panel__tagline">Carpets and flooring supplied and fitted</div>
  </div>
  <div class="block back__band-bottom"></div>
</section>

</body>
</html>
```